Help our Velvet Parlour find our winning design! We're looking for a business card....

We’re a Velvet Parlour in NY specializing in custom-made cakes and unique desserts.
Our cakes combine flavor and art, each designed to match customer’s special event and theme.
We’d like a unique business card with a clean design that will combine French chic and artistic look & feel.
We’d like to differentiate ourselves from standard bakeries, please don’t offer cupcake images :-)
Our logo is peach-pink and brown and we’d love to use these colors ( . Another color that can be added is gold - or feel free to suggest!

Target Market(s)

Women, ages 25-55

Industry/Entity Type

Boutique

Contact Information for Business Card

Text on card:
Logo
Velvet Parlour by Nadia Fenwick

www.xxxxxxxx.com
xxx@xxxxx.com
(555) xxx-xxxx
F – xxxxxxxxxx
IG - xxxxxxxxx

Font styles to use
Sans Serif
Script

Requirements
Must have
• Logo
• Clean look
• French chic and artistic look & feel.
Nice to have
• Damask pattern
Should not have
• Cupcake images

```html
<!DOCTYPE html>
<html lang="en">
<head>
<meta charset="utf-8">
<title>Velvet Parlour – Business Card</title>
<link rel="stylesheet" href="https://fonts.googleapis.com/css2?family=Great+Vibes&family=Lato:wght@400&display=swap">
<style>
  :root {
    --stage: #4b4b4b;
    --cocoa: #3a2620;
    --cocoa-pattern: #4a3129;
    --blush: #fbe5df;
    --peach: #f0a593;
    --gold-dark: #b89a62;
    --gold-light: #ead3a0;
  }
  html, body {
    margin: 0;
    padding: 0;
    width: 1200px;
    height: 1000px;
    overflow: hidden;
    background: var(--stage);
  }
  .canvas {
    position: relative;
    width: 1200px;
    height: 1000px;
  }
  .card {
    position: absolute;
    top: 174px;
    width: 409px;
    height: 663px;
    overflow: hidden;
  }
  .card--back { left: 150px; }
  .card--front { left: 622px; }

  .damask-field {
    position: absolute;
    left: 0;
    right: 0;
    background: var(--cocoa);
    background-image: radial-gradient(circle at 50% 50%, var(--cocoa-pattern) 0%, var(--cocoa) 70%);
  }
  .card--back .damask-field { top: 0; bottom: 0; }
  .card--front .damask-field { top: 347px; bottom: 0; }

  .brand-name {
    position: absolute;
    left: 0;
    right: 0;
    text-align: center;
    font-family: "Lato", sans-serif;
    font-weight: 400;
    font-size: 30px;
    letter-spacing: 2px;
  }
  .card--back .brand-name { top: 330px; color: var(--blush); }
  .card--front .brand-top {
    position: absolute;
    top: 0; left: 0; right: 0;
    height: 324px;
    background: var(--blush);
  }
  .card--front .brand-name { top: 186px; color: var(--cocoa); }

  .gold-band {
    position: absolute;
    top: 324px;
    left: 0;
    right: 0;
    height: 23px;
    background: linear-gradient(90deg, var(--gold-dark) 0%, var(--gold-light) 50%, var(--gold-dark) 100%);
  }

  .owner-name {
    position: absolute;
    top: 382px;
    left: 0;
    right: 0;
    text-align: center;
    font-family: "Great Vibes", cursive;
    font-size: 44px;
    color: var(--peach);
  }
  .contact-list {
    position: absolute;
    top: 474px;
    left: 0;
    right: 0;
    margin: 0;
    padding: 0;
    list-style: none;
    text-align: center;
    font-family: "Lato", sans-serif;
    font-size: 17px;
    color: var(--peach);
  }
  .contact-list li {
    height: 27.5px;
    display: flex;
    align-items: center;
    justify-content: center;
    gap: 7px;
  }
  .contact-icon {
    width: 15px;
    height: 15px;
    flex: none;
  }
  .social-dot {
    width: 11px;
    height: 11px;
    border-radius: 50%;
    background: var(--peach);
    flex: none;
  }
</style>
</head>
<body>
<main class="canvas">
  <section class="card card--back">
    <div class="damask-field" role="img" aria-label="Brown damask pattern background"></div>
    <div class="brand-name">Velvet Parlour</div>
  </section>

  <section class="card card--front">
    <div class="brand-top"></div>
    <div class="brand-name">Velvet Parlour</div>
    <div class="gold-band"></div>
    <div class="damask-field" role="img" aria-label="Brown damask pattern background"></div>
    <div class="owner-name">Nadia Fenwick</div>
    <ul class="contact-list">
      <li>
        <svg class="contact-icon" viewBox="0 0 16 16" aria-hidden="true"><rect x="4" y="1" width="8" height="14" rx="1.5" fill="none" stroke="#f0a593" stroke-width="1.5"/><circle cx="8" cy="12.5" r="0.9" fill="#f0a593"/></svg>
        (555) 014-2290
      </li>
      <li>
        <svg class="contact-icon" viewBox="0 0 16 16" aria-hidden="true"><rect x="1" y="3" width="14" height="10" fill="#f0a593"/><path d="M1 3 L8 9 L15 3" fill="none" stroke="#3a2620" stroke-width="1.2"/></svg>
        nadia@VelvetParlourNY.com
      </li>
      <li>
        <svg class="contact-icon" viewBox="0 0 16 16" aria-hidden="true"><circle cx="8" cy="8" r="6.5" fill="none" stroke="#f0a593" stroke-width="1.5"/><ellipse cx="8" cy="8" rx="2.8" ry="6.5" fill="none" stroke="#f0a593" stroke-width="1.2"/><line x1="1.5" y1="8" x2="14.5" y2="8" stroke="#f0a593" stroke-width="1.2"/></svg>
        www.VelvetParlourNY.com
      </li>
      <li><span class="social-dot"></span>VelvetParlourCakes</li>
      <li><span class="social-dot"></span>VelvetParlourCakes</li>
    </ul>
  </section>
</main>
</body>
</html>
```